Crust Harbor Hotel Coupon

Would like to design a coupon that is for hotels' staff and to be dropped off at the hotel front office anytime someone calls from a hotel and as a Thank You for hotel staff for recommending us. Coupon value to be $ 2.00. Should say Thank You or Thank you for recommending us. Need our phone number 250 614 3750 on it. Color scheme to be Green and Red as in the attached logo. Coupon to be designed for printing size 3.5 inches high and 7.5 inches wide. Rear should say Fastest Delivery, Favourite Pizza for Sports teams etc. Ask for group deals. Attached logo to be on the coupon. Coupon should say coupon # and space left for us write number

```html
<!DOCTYPE html>
<html lang="en">
<head>
<meta charset="utf-8">
<title>Crust Harbor Hotel Coupon</title>
<link rel="stylesheet" href="https://fonts.googleapis.com/css2?family=Bebas+Neue&family=Kaushan+Script&family=Yellowtail&family=Lato:wght@400&display=swap">
<style>
  :root {
    --page: #ffffff;
    --coupon-red: #d9232d;
    --coupon-green: #1e9a3c;
    --coupon-white: #ffffff;
    --crust-light: #e9a85a;
    --crust-mid: #c9682e;
    --crust-dark: #9a3b1c;
  }
  html, body {
    margin: 0;
    width: 1200px;
    height: 1200px;
    overflow: hidden;
    background: var(--page);
  }
  .canvas {
    position: relative;
    width: 1200px;
    height: 1200px;
  }
  .coupon {
    position: absolute;
    left: 74px;
    top: 355px;
    width: 1051px;
    height: 490px;
    display: block;
  }
  .coupon-bg { fill: var(--coupon-red); }
  .cut-line {
    fill: none;
    stroke: var(--coupon-white);
    stroke-width: 1.2;
    stroke-dasharray: 5 4;
    opacity: 0.85;
  }
  .label {
    font-family: "Bebas Neue", sans-serif;
    fill: var(--coupon-green);
  }
  .figure {
    font-family: "Bebas Neue", sans-serif;
    fill: var(--coupon-white);
  }
  .tagline {
    font-family: "Bebas Neue", sans-serif;
    font-size: 23px;
    fill: var(--coupon-white);
    letter-spacing: 0.2px;
  }
  .thanks {
    font-family: "Yellowtail", "Kaushan Script", cursive;
    font-size: 92px;
    fill: var(--coupon-white);
  }
  .thanks-note {
    font-family: "Lato", sans-serif;
    font-size: 21px;
    fill: var(--coupon-white);
  }
  .brand-name {
    font-family: "Bebas Neue", sans-serif;
    font-size: 46px;
    fill: var(--coupon-white);
  }
  .brand-dot { fill: var(--coupon-green); }
</style>
</head>
<body>
<main class="canvas">
  <svg class="coupon" viewBox="0 0 1051 490" xmlns="http://www.w3.org/2000/svg">
    <defs>
      <radialGradient id="pizza-tones" cx="0.5" cy="0.5" r="0.5">
        <stop offset="0" stop-color="#c9682e"/>
        <stop offset="0.85" stop-color="#9a3b1c"/>
        <stop offset="1" stop-color="#e9a85a"/>
      </radialGradient>
      <clipPath id="coupon-clip">
        <rect width="1051" height="490"/>
      </clipPath>
    </defs>

    <rect class="coupon-bg" width="1051" height="490"/>

    <path class="cut-line" d="M750 26 H31 V462 H500"/>

    <g clip-path="url(#coupon-clip)">
      <circle cx="810" cy="512" r="322" fill="url(#pizza-tones)" role="img" aria-label="Photo of a supreme pizza with pepperoni, mushrooms, green peppers and sausage"/>
    </g>

    <g class="brand" transform="translate(750 78)">
      <circle class="brand-dot" cx="12" cy="0" r="12"/>
      <text class="brand-name" x="32" y="16">Crust Harbor</text>
    </g>

    <text class="label" x="66" y="137" font-size="50">Coupon value to be</text>
    <text class="figure" x="422" y="137" font-size="114">$ 2.00</text>

    <text class="label" x="68" y="221" font-size="48">Call us:</text>
    <text class="figure" x="200" y="221" font-size="70">250 614 3750</text>

    <text class="tagline" x="66" y="269">Fastest delivery, favourite pizza for sports teams etc.</text>
    <text class="tagline" x="66" y="295">Ask for group deals.</text>

    <text class="thanks" x="64" y="389">Thank you</text>
    <text class="thanks-note" x="65" y="423">For recommending us</text>
  </svg>
</main>
</body>
</html>
```